Webdesign/Updates

We would like a landing page for an online course for our educators. So a website with about 3 to 5 pages - Home, About US, Online course, blog, and Contact us. We have a wordpress site up using a template, but we are looking for something that connects more with our new logo.

Target Market(s)

Educators, workshop trainers/instructors, colleges, community schools, educational institutions, global organizations

Industry/Entity Type

Education

Contact Information for Business Card

Use the words below as place holders for the front:
Name
Title
Address line 1
Address line 2
Email
Phone
Website URL

--the back
Logo
1 short question, use "What do you 1234 about your program?"

Number of Pages Required

4 page

Requirements
Must have
• Home page
• Course Page
• Blog
• right side bar with social media content and invitation to subscribe to newsletter
• see logo colors in document
Nice to have
• Newsletter Page with graphic that can be on this page or page can be sent as a pdf via email or in an email.
Should not have
• Be better than attached description
• clean simple look but stylish

```html
<!DOCTYPE html>
<html lang="en">
<head>
<meta charset="utf-8">
<title>About – Skill Craft School</title>
<link href="https://fonts.googleapis.com/css2?family=Montserrat:wght@400;500;600;700;800&display=swap" rel="stylesheet">
<style>
:root{
  --blue:#1ea8e0;
  --green:#a9cd3a;
  --orange:#f05a28;
  --ink:#111111;
  --text:#333333;
  --muted:#9a9a9a;
  --rule:#e2e2e2;
  --paper:#ffffff;
  --btn-friendwall:#3b5697;
  --btn-chirpline:#4aa9ec;
  --btn-pinloft:#c01f26;
  --btn-photolane:#a3258c;
  --btn-circlecast:#d54233;
  --btn-workhub:#2d6aad;
  --btn-vidstream:#b81619;
  --btn-rss:#e9880f;
}
*{box-sizing:border-box;margin:0;padding:0}
html,body{width:867px;height:1200px;overflow:hidden;background:var(--paper)}
body{position:relative;font-family:"Montserrat",sans-serif;color:var(--text)}
.abs{position:absolute}

/* header */
.site-header{left:0;top:0;width:867px;height:56px;background:rgba(248,248,248,.96);z-index:2}
.brand{left:169px;top:20px;font-weight:800;font-size:14.5px;letter-spacing:1.2px;color:var(--blue)}
.main-nav{left:446px;top:24px;display:flex;gap:0}
.main-nav a{font-size:6.4px;font-weight:600;letter-spacing:1px;color:var(--ink);text-decoration:none;position:relative}
.main-nav a:nth-child(1){margin-right:26px}
.main-nav a:nth-child(2){margin-right:26px}
.main-nav a:nth-child(3){margin-right:26px}
.main-nav a:nth-child(4){margin-right:27px}
.main-nav a.is-active::after{content:"";position:absolute;left:-13px;right:-13px;top:13px;height:2px;
  background:linear-gradient(90deg,var(--blue) 0 33%,var(--green) 33% 66%,var(--orange) 66%)}

/* hero */
.hero{left:0;top:56px;width:867px;height:225px;
  background:linear-gradient(100deg,#2a2a2a 0%,#4a4a48 14%,#d9d7d8 30%,#cfcccd 55%,#bdb9ba 75%,#a9a5a6 100%)}
.hero-desk{left:0;top:236px;width:867px;height:45px;background:linear-gradient(180deg,#3a3a3a,#1d1d1d)}
.page-badge{left:169px;top:201px;width:90px;height:42px;background:rgba(30,30,30,.9);
  color:#fff;font-weight:700;font-size:14px;letter-spacing:.5px;padding:12px 0 0 25px}
.page-badge::before{content:"";position:absolute;left:17px;top:10px;width:2px;height:22px;
  background:linear-gradient(180deg,var(--blue),var(--green),var(--orange))}

/* intro */
.page-title{left:169px;top:307px;font-weight:700;font-size:15.5px;color:var(--ink);letter-spacing:.3px}
.page-sub{left:169px;top:326px;font-size:9px;color:var(--blue);letter-spacing:.3px}

/* content */
.photo{background:linear-gradient(180deg,#d8d3cc 0%,#cbbfae 40%,#8f8a7c 62%,#7a7a55 78%,#5e5e33 100%)}
.photo-city{left:169px;top:358px;width:353px;height:179px}
.photo-person{left:169px;top:692px;width:157px;height:203px;
  background:linear-gradient(180deg,#5a5650 0%,#6c6963 40%,#7f9bb8 70%,#6a87a6 100%)}
.copy p{font-size:7.3px;line-height:11.7px;color:var(--text)}
.copy p+p{margin-top:11.7px}
.copy-a{left:169px;top:551px;width:353px}
.feature-head{left:345px;top:691px;width:177px;font-weight:700;font-size:10px;line-height:12px;color:var(--ink)}
.copy-b{left:345px;top:726px;width:177px}
.copy-c{left:169px;top:907px;width:353px}

/* sidebar */
.subscribe{left:543px;top:358px;width:155px;height:179px;border:1px solid #d4d4d4;background:#fff}
.tricolor{position:absolute;left:-1px;right:-1px;height:4px;
  background:linear-gradient(90deg,var(--blue) 0 33.3%,var(--green) 33.3% 66.6%,var(--orange) 66.6%)}
.tricolor.top{top:-1px;height:7px}
.tricolor.bottom{bottom:-1px;height:3px}
.subscribe h3{position:absolute;left:8px;right:8px;top:27px;text-align:center;font-size:7.6px;
  line-height:8px;font-weight:600;color:var(--ink)}
.field{position:absolute;left:20px;width:114px;height:15px;border:1px solid #d6d6d6;
  font-size:4.8px;color:#666;padding:4.5px 5px}
.btn-get{position:absolute;left:20px;top:134px;width:114px;height:17px;background:var(--blue);
  color:#fff;font-size:6px;font-weight:800;text-align:center;line-height:17px;letter-spacing:.3px}
.social{left:546px;top:549px;width:149px;display:grid;grid-template-columns:73px 73px;column-gap:2px;row-gap:3.5px}
.social a{height:22px;border-radius:3px;color:#fff;font-size:6px;font-weight:600;text-decoration:none;
  display:flex;align-items:center;justify-content:center;box-shadow:inset 0 -2px 0 rgba(0,0,0,.18)}
.s-friendwall{background:var(--btn-friendwall)}.s-chirpline{background:var(--btn-chirpline)}
.s-pinloft{background:var(--btn-pinloft)}.s-photolane{background:var(--btn-photolane)}
.s-circlecast{background:var(--btn-circlecast)}.s-workhub{background:var(--btn-workhub)}
.s-vidstream{background:var(--btn-vidstream)}.s-rss{background:var(--btn-rss)}

/* footer */
.footer-rule{left:169px;top:1061px;width:529px;height:1px;background:var(--rule)}
.footer-brand{left:0;width:867px;top:1078px;text-align:center;font-weight:800;font-size:14.5px;letter-spacing:1.2px;color:var(--blue)}
.footer-nav{left:282px;top:1116px;display:flex}
.footer-nav a{font-size:6.4px;font-weight:600;letter-spacing:1px;color:var(--ink);text-decoration:none}
.footer-nav a+a{margin-left:38px}
.bottom-bar{left:0;top:1166px;width:867px;height:34px;background:var(--blue);color:#fff;font-size:5.8px}
.bottom-bar .left{position:absolute;left:169px;top:14px}
.bottom-bar .right{position:absolute;right:169px;top:14px}
.bottom-bar b{font-weight:700}
</style>
</head>
<body>

<header class="abs site-header">
  <div class="abs brand">SKILL CRAFT SCHOOL</div>
  <nav class="abs main-nav">
    <a href="#">HOME</a><a href="#">COURSE</a><a href="#">BLOG</a><a href="#">CONSULTING</a><a href="#" class="is-active">ABOUT</a>
  </nav>
</header>

<div class="abs hero" role="img" aria-label="Desk scene with a potted plant in a jar, a laptop and a keyboard"></div>
<div class="abs hero-desk" aria-hidden="true"></div>
<div class="abs page-badge">ABOUT</div>

<h1 class="abs page-title">SKILL CRAFT SCHOOL</h1>
<div class="abs page-sub">Company Profile</div>

<div class="abs photo photo-city" role="img" aria-label="City skyline across the water at sunset, with a park and a bare tree"></div>

<div class="abs copy copy-a">
  <p>Vestibulum in posuere quam. Donec sollicitudin massa sed orci mattis tincidunt. Fusce a libero vitae tellus molestie tempor. Proin a dui lorem. Aliquam fringilla a ex non aliquet. Etiam efficitur dapibus imperdiet. Nam maximus condimentum mauris eget consectetur. Nam odio lacus, viverra bibendum mauris vitae, scelerisque consequat dui. Duis vel purus imperdiet, ullamcorper ex sit amet, porta elit.</p>
  <p>Lorem ipsum dolor sit amet, consectetur adipiscing elit. Morbi ante nisl, tempor vitae est eget, tincidunt auctor nulla. Curabitur semper, augue ac cursus condimentum, eros eros tempus massa, eget euismod ante nisl sit amet tortor. Fusce congue enim lectus. Fusce id pellentesque libero. Nam id metus auctor, consectetur tortor sit amet, accumsan odio.</p>
</div>

<div class="abs photo photo-person" role="img" aria-label="Portrait of a smiling team member in a denim shirt in an office"></div>
<h2 class="abs feature-head">Vestibulum in posuere quam. Donec sollicitudin</h2>
<div class="abs copy copy-b">
  <p>massa sed orci mattis tincidunt. Fusce a libero vitae tellus molestie tempor. Proin a dui lorem. Aliquam fringilla a ex non aliquet. Etiam efficitur dapibus imperdiet. Nam maximus condimentum mauris eget consectetur. Nam odio lacus, viverra bibendum mauris vitae, scelerisque consequat dui. Duis vel purus imperdiet, ullamcorper ex sit amet, porta elit.</p>
  <p>Lorem ipsum dolor sit amet, consectetur adipiscing elit. Morbi ante nisl, tempor vitae est eget, tincidunt auctor nulla. Curabitur semper, augue ac cursus condimentum, eros eros tempus massa, eget euismod ante nisl sit amet tortor.</p>
</div>

<div class="abs copy copy-c">
  <p>Fusce sollicitudin venenatis eros, eget suscipit dui iaculis quis. Sed et tortor sagittis, vehicula sem ut, dignissim magna. Cras id nisi quis erat iaculis faucibus. Donec aliquet, nisl vitae vulputate scelerisque, orci sem dictum orci, sit amet imperdiet diam sem nec tellus. Nunc non velit nunc. Etiam in ante ut lacus scelerisque convallis eu eget mauris. Integer imperdiet lectus in fermentum convallis. Nunc efficitur tristique dui, eu sodales lacus. In bibendum lorem ut mauris ornare fermentum.</p>
  <p>Maecenas mollis lorem nec nunc fringilla, quis tempus ipsum mollis. Donec sed fermentum mi. Quisque accumsan semper dui in tincidunt. In efficitur risus id nibh sollicitudin semper. Aliquam placerat nisl nec vehicula posuere.</p>
</div>

<aside class="abs subscribe">
  <span class="tricolor top"></span>
  <h3>Join our community of student around the world helping you to succeed.</h3>
  <div class="field" style="top:70px">Your Name*</div>
  <div class="field" style="top:89px">Email*</div>
  <div class="field" style="top:108px">Phone*</div>
  <div class="btn-get">GET IT NOW</div>
  <span class="tricolor bottom"></span>
</aside>

<nav class="abs social">
  <a href="#" class="s-friendwall">Friendwall</a>
  <a href="#" class="s-chirpline">Chirpline</a>
  <a href="#" class="s-pinloft">Pinloft</a>
  <a href="#" class="s-photolane">Photolane</a>
  <a href="#" class="s-circlecast">Circlecast</a>
  <a href="#" class="s-workhub">Workhub</a>
  <a href="#" class="s-vidstream">Vidstream</a>
  <a href="#" class="s-rss">RSS Feed</a>
</nav>

<div class="abs footer-rule"></div>
<div class="abs footer-brand">SKILL CRAFT SCHOOL</div>
<nav class="abs footer-nav">
  <a href="#">HOME</a><a href="#">COURSE</a><a href="#">BLOG</a><a href="#">CONSULTING</a><a href="#">ABOUT</a>
</nav>

<footer class="abs bottom-bar">
  <span class="left">Copyright 2018 <b>Skill Craft School</b></span>
</footer>

</body>
</html>
```